New Slide Master Template for PPT

I need a new Slide Master / Template for PPT presentations. Our company does Cloud Management / Network Management systems that are used to manage devices connected to the internet. Those devices can be things like Wireless Access Points, DSL modems, Cable modems, Gateways, Routers, Switches, and the equipment that is in the internet such as Varnex, Thistle, or Morvane-Quist equipment.
What our management system does is connect/communicate with all these different devices to be able to get information from the devices such as throughput performance, wireless coverage, failures conditions, firmware versions, and any other information which is used to manage, control, or troubleshoot those devices for the equipment companies or internet service providers who have provided them to their end customers for internet service.
The new Slide Master / Template for PowerPoint needs to do to the following;
1. be fresh and current in design
2. have a nice looking font that works for both print and presentation on small screens (laptops) as well as big screen (large group presentations)
3. not consume too many MegaBytes when saved as a file. Many email servers have limits on the size of files which can be transferred as an attachment. Most are either 5 or 10 MB limits. I do not want to have to zip the file to get it under such size restrictions.
4. the colors in the "Brovatel" logo are the company colors (the orange and blue), those should be incorporated in some form in the Slide Master / Template.
5. the final design should communicate professionalism with a modern look and feel.
6. once done the attached (old version of presentation) should be transferred over using the new Slide Master / Template and new fonts.
NOTE: I am not seeing how to attach my current PPT file to this project. Please email me at daniel@pinegatesystems.example and I will send you the current presentation which needs to be updated as described above.
Target Market(s)
Networking equipment manufacturers like Varnex, Pravlink, Morvane-Quist, Voxnet, etc.
Industry/Entity Type
Internet
Look and feel
Each slider illustrates characteristics of the customer's brand and the style your logo design should communicate.

```html
<!DOCTYPE html>
<html lang="en">
<head>
<meta charset="utf-8">
<title>WiFi Network Management: Maps and Topology</title>
<link rel="stylesheet" href="https://fonts.googleapis.com/css2?family=Graduate&family=Arimo:wght@400;700&display=swap">
<style>
  :root {
    --orange: #f5ad3c;
    --orange-deep: #f29a1f;
    --ink: #2e2e2e;
    --text-grey: #555555;
    --panel: #333333;
    --blue: #1e6fba;
    --black: #111111;
    --white: #ffffff;
  }
  * { margin: 0; padding: 0; box-sizing: border-box; }
  html, body { width: 960px; height: 1200px; overflow: hidden; background: var(--white); }
  .slide { position: relative; width: 960px; height: 1200px; font-family: "Arimo", Arial, sans-serif; }

  .step-badge { position: absolute; left: 16px; top: 348px; width: 88px; height: 116px; }
  .step-badge span {
    position: absolute; left: 0; top: 14px; width: 88px; text-align: center;
    font-family: "Arimo", Arial, sans-serif; font-weight: 700; font-size: 64px; color: var(--white);
  }

  .title { position: absolute; left: 126px; top: 368px; font-family: "Graduate", "Arial Black", serif; font-weight: 400; line-height: 1; white-space: nowrap; }
  .title-kicker { color: var(--orange-deep); font-size: 33px; letter-spacing: 0.3px; }
  .title-main { color: var(--ink); font-size: 35px; margin-top: 11px; letter-spacing: 0; }

  .feature { position: absolute; top: 490px; padding-left: 26px; color: var(--text-grey); font-size: 16.5px; line-height: 1.25; }
  .feature::before { content: ""; position: absolute; left: 0; top: 6px; width: 9px; height: 9px; background: var(--orange); }
  .feature-left { left: 54px; width: 360px; }
  .feature-right { left: 514px; width: 430px; font-size: 16px; }
  .feature-divider { position: absolute; left: 452px; top: 484px; width: 2px; height: 46px; background: var(--ink); }

  .screens { position: absolute; left: 12px; top: 539px; width: 935px; height: 259px; background: var(--panel); border-radius: 10px; }
  .screen { position: absolute; top: 12px; height: 241px; }
  .screen-campus { left: 12px; width: 238px; background: linear-gradient(160deg, #e9ece6 0%, #2f9a4a 45%, #2c8a43 70%, #e4e6e2 100%); }
  .screen-floors { left: 257px; width: 335px; background: linear-gradient(180deg, #f6f6f4 0%, #ecebe6 100%); }
  .screen-heatmap { left: 599px; width: 329px; background: radial-gradient(circle at 50% 45%, #8fb5e8 0%, #3f7fd6 55%, #2a62c4 100%); }

  .footer-band { position: absolute; left: 0; top: 802px; width: 960px; height: 38px; background: var(--orange); }
  .footer-rule { position: absolute; left: 0; top: 842px; width: 960px; height: 12px; background: var(--blue); }
  .site-link {
    position: absolute; left: 0; top: 813px; width: 268px; height: 41px; background: var(--black);
    color: var(--white); font-size: 17px; font-weight: 700; line-height: 41px; padding-left: 9px; white-space: nowrap;
  }
  .site-link em { font-style: normal; color: var(--orange); }
  .brand {
    position: absolute; left: 738px; top: 813px; width: 222px; height: 53px; background: var(--black);
    display: flex; align-items: center; gap: 10px; padding-left: 16px;
  }
  .brand-dot { width: 24px; height: 24px; border-radius: 50%; background: var(--blue); flex: none; }
  .brand-text { display: flex; flex-direction: column; line-height: 1; }
  .brand-name { color: var(--white); font-size: 24px; font-weight: 700; }
  .brand-sub { color: var(--white); font-size: 9px; font-weight: 400; letter-spacing: 2.6px; margin-top: 3px; }
</style>
</head>
<body>
<div class="slide">
  <svg class="step-badge" viewBox="0 0 88 116" aria-hidden="true">
    <polygon points="0,0 88,0 88,116 44,92 0,116" fill="#f5ad3c"/>
  </svg>
  <div class="step-badge"><span>4</span></div>

  <h1 class="title">
    <div class="title-kicker">WIFI NETWORK</div>
    <div class="title-main">MANAGEMENT : MAPS AND TOPOLOGY</div>
  </h1>

  <p class="feature feature-left">Provides multiple layers of maps in campus, building and floor</p>
  <div class="feature-divider"></div>
  <p class="feature feature-right">Provides tooltips on information for AC, AP and clients summary info in each map</p>

  <div class="screens">
    <div class="screen screen-campus" role="img" aria-label="Campus map screenshot with building tooltip showing floors, access points, radios and client counts"></div>
    <div class="screen screen-floors" role="img" aria-label="Floor list screenshot with floor plan thumbnails and details of access points, radios, alarms and clients"></div>
    <div class="screen screen-heatmap" role="img" aria-label="Wireless coverage heatmap screenshot showing access points linked on a floor plan"></div>
  </div>

  <div class="footer-band"></div>
  <div class="footer-rule"></div>
  <div class="site-link">http://www.<em>brovatel</em>.example</div>
  <div class="brand">
    <div class="brand-dot"></div>
    <div class="brand-text">
      <span class="brand-name">Brovatel</span>
      <span class="brand-sub">TECHNOLOGIES</span>
    </div>
  </div>
</div>
</body>
</html>
```